I own a rendering company which is in the construction industry i already have a logo i would like i

I want to make the website look professional and blends nicely with the logo, if i can have contact information and photos logos and a place where they can email me for job quotes or request and we want to win the big jobs so think also corporate in conjunction with construction. also an area for brief description and about us

Target Market(s)

Home owners/Investors, Small and major construction companies

Industry/Entity Type

Construction Company

Font styles to use
Serif
Sans Serif

Colors

Designer to choose colors to be used in the design.

Requirements
Must have
• An area for pictures to show with fade changes or clicking options(of white set walls, acrylic render expensive houses walls) an "about us" section. An area to where potential customers can email us (a writing box) where we can receive request for quotes and potential jobs. all contact information and license numbers
Nice to have
• pictures of plastered walls (posh elegant) and rendered walls acrylic and cement render
Should not have
• anything boring plain font etc

```html
<!DOCTYPE html>
<html lang="en">
<head>
<meta charset="utf-8">
<title>Kestrel Rendering</title>
<link href="https://fonts.googleapis.com/css2?family=Montserrat:wght@400;600;700&family=Open+Sans:wght@400;600&display=swap" rel="stylesheet">
<style>
:root{
  --red:#e31e25;
  --ink:#1b1b1b;
  --muted:#555;
  --navy:#1c2430;
  --line:#e2e2e2;
  --white:#fff;
}
*{box-sizing:border-box;margin:0;padding:0}
html,body{width:1200px;height:3152px;overflow:hidden}
body{font-family:'Open Sans',Arial,sans-serif;color:var(--ink);background:var(--white);position:relative}
.head{font-family:'Montserrat',Arial,sans-serif}
a{color:inherit;text-decoration:none}
.btn{display:inline-block;background:var(--red);color:#fff;font-family:'Montserrat',Arial,sans-serif;font-weight:700;font-size:11px;letter-spacing:.5px;text-transform:uppercase;padding:0 16px;height:24px;line-height:24px}
.rule{width:48px;height:3px;background:var(--red);margin:14px auto 0}
.section-title{font-family:'Montserrat',Arial,sans-serif;font-weight:700;font-size:21px;text-align:center;letter-spacing:.5px}

/* header */
.site-header{position:absolute;left:0;top:0;width:1200px;height:137px}
.brand{position:absolute;left:132px;top:22px;display:flex;align-items:center;gap:12px}
.brand-mark{width:26px;height:26px;background:var(--red)}
.brand-name{font-family:'Montserrat',Arial,sans-serif;font-weight:700;color:var(--red);font-size:24px;line-height:28px;letter-spacing:1px}
.call{position:absolute;left:728px;top:26px;display:flex;align-items:center;gap:12px}
.call-icon{width:34px;height:34px;border-radius:50%;background:#333;display:flex;align-items:center;justify-content:center}
.call small{display:block;font-family:'Montserrat',Arial,sans-serif;font-size:10px;font-weight:600;color:#333}
.call strong{display:block;font-family:'Montserrat',Arial,sans-serif;font-size:22px;font-weight:600;color:var(--red);line-height:24px}
.search{position:absolute;left:950px;top:28px;width:120px;height:33px;border:1px solid #ccc;display:flex;align-items:center;gap:8px;padding-left:12px;font-size:9px;font-family:'Montserrat',Arial,sans-serif;color:#444}
.nav{position:absolute;right:128px;top:89px;display:flex;height:48px;border-top:1px solid var(--line)}
.nav a{font-family:'Montserrat',Arial,sans-serif;font-weight:600;font-size:12px;padding:0 22px;line-height:48px;color:#222}
.nav a.active{background:var(--red);color:#fff}

/* hero */
.hero{position:absolute;left:0;top:137px;width:1200px;height:535px;background:linear-gradient(90deg,#3d434b 0%,#2f353d 50%,#262b32 100%)}
.hero-copy{position:absolute;left:0;right:0;top:250px;text-align:center;color:#fff}
.hero-copy h1{font-family:'Montserrat',Arial,sans-serif;font-weight:600;font-size:33px;line-height:42px;letter-spacing:.5px}
.hero-copy .btn{margin-top:20px;height:50px;line-height:46px;font-size:15px;padding:0 28px;border:2px solid #fff}
.dots{position:absolute;top:592px;left:0;right:0;display:flex;justify-content:center;gap:14px}
.dots span{width:10px;height:10px;border-radius:50%;background:#fff}
.dots span.on{background:var(--red);box-shadow:0 0 0 2px #fff}

/* services */
.services{position:absolute;left:0;top:672px;width:1200px;height:526px}
.services .section-title{margin-top:44px}
.service-grid{position:absolute;left:132px;top:133px;display:flex}
.service{width:318px;text-align:center;padding:0 8px}
.service+.service{border-left:1px solid var(--line)}
.service .ph{height:200px;margin:0 8px}
.service h3{font-family:'Montserrat',Arial,sans-serif;font-weight:700;font-size:13px;margin-top:26px}
.service p{font-size:11px;line-height:16px;color:var(--muted);margin:10px auto 0;width:220px}
.service .btn{margin-top:18px;font-size:9px;height:22px;line-height:22px}

/* about */
.about{position:absolute;left:0;top:1198px;width:1200px;height:442px;background:linear-gradient(90deg,#a58a5a 0%,#c4a56f 40%,#d8d2c6 62%,#c8b38a 100%)}
.about-copy{position:absolute;left:132px;top:72px;width:372px;color:#fff}
.about-copy .eyebrow{font-family:'Montserrat',Arial,sans-serif;font-weight:700;font-size:17px}
.about-copy h2{font-family:'Montserrat',Arial,sans-serif;font-weight:700;font-size:29px;margin-top:6px}
.about-copy p{font-size:12px;line-height:20px;margin-top:16px;text-align:justify}
.about-copy .btn{margin-top:40px;font-size:9px}

/* blog */
.blog{position:absolute;left:0;top:1640px;width:1200px;height:592px}
.blog .section-title{margin-top:46px}
.blog-grid{position:absolute;left:134px;top:142px;display:flex;gap:22px}
.post{width:296px;height:387px;border:1px solid var(--line)}
.post .ph{height:214px}
.post h3{font-family:'Montserrat',Arial,sans-serif;font-weight:700;font-size:12px;line-height:17px;margin:28px 24px 0}
.post p{font-size:10px;line-height:15px;color:var(--muted);margin:8px 24px 0}
.post .btn{margin:16px 24px 0;font-size:9px;height:24px;line-height:24px}

/* contact */
.contact{position:absolute;left:0;top:2232px;width:1200px;height:521px;background:linear-gradient(180deg,#8e8e8e 0%,#6c6c6c 60%,#5a5a5a 100%)}
.contact-card{position:absolute;left:313px;top:52px;width:572px;height:425px;background:#fff;box-shadow:0 6px 24px rgba(0,0,0,.25);text-align:center}
.contact-card .section-title{margin-top:42px}
.form{position:absolute;left:61px;top:118px;width:450px}
.row{display:flex;gap:18px;margin-bottom:16px}
.field{flex:1;height:40px;border:1px solid #bbb;text-align:left;font-size:11px;padding:11px 14px;color:#333}
.field.area{height:94px}
.form .btn{margin-top:8px;height:36px;line-height:36px;font-size:13px;padding:0 24px}

/* footer */
.site-footer{position:absolute;left:0;top:2753px;width:1200px;height:399px;background:var(--navy);color:#fff}
.footer-brand{position:absolute;left:132px;top:70px;width:200px;text-align:center}
.footer-brand .brand-name{font-size:30px;line-height:36px}
.footer-brand .brand-mark{width:34px;height:34px;margin:0 auto 14px}
.license{position:absolute;left:132px;top:218px;width:200px;text-align:center;font-size:11px}
.col{position:absolute;top:62px}
.col h4{font-family:'Montserrat',Arial,sans-serif;font-weight:700;font-size:11px;color:var(--red);margin-bottom:22px}
.col-contact{left:426px}
.c-item{display:flex;gap:12px;font-size:11px;line-height:16px;margin-bottom:18px}
.c-item svg{flex:none;margin-top:2px}
.col-menu{left:703px}
.col-menu li{list-style:none;font-size:11px;line-height:18px}
.col-news{left:861px}
.col-news .field{width:208px;background:#fff;border:none;height:40px;font-size:11px;padding:12px 14px}
.col-news .btn{margin-top:18px;font-size:11px;height:30px;line-height:30px}
.footer-rule{position:absolute;left:132px;right:132px;top:271px;height:1px;background:#3a4453}
.follow{position:absolute;left:136px;top:315px;display:flex;align-items:center;gap:10px;font-family:'Montserrat',Arial,sans-serif;font-weight:700;font-size:11px}
.follow span.dot{width:24px;height:24px;border-radius:50%}
.copyright{position:absolute;right:132px;top:320px;font-size:10px}
</style>
</head>
<body>

<header class="site-header">
  <div class="brand">
    <span class="brand-mark"></span>
    <span class="brand-name">KESTREL<br>RENDERING</span>
  </div>
  <div class="call">
    <span class="call-icon">
      <svg width="16" height="16" viewBox="0 0 24 24"><path fill="#fff" d="M6.6 10.8a15.1 15.1 0 0 0 6.6 6.6l2.2-2.2c.3-.3.7-.4 1-.2 1.1.4 2.3.6 3.6.6.6 0 1 .4 1 1V20c0 .6-.4 1-1 1C10.6 21 3 13.4 3 4c0-.6.4-1 1-1h3.5c.6 0 1 .4 1 1 0 1.3.2 2.5.6 3.6.1.3 0 .7-.2 1z"/></svg>
    </span>
    <div><small>CALL US NOW</small><strong>555.014.2288</strong></div>
  </div>
  <div class="search">
    <svg width="10" height="10" viewBox="0 0 24 24"><circle cx="10" cy="10" r="7" fill="none" stroke="#444" stroke-width="3"/><path d="M15 15l6 6" stroke="#444" stroke-width="3"/></svg>
    SEARCH
  </div>
  <nav class="nav">
    <a class="active">HOME</a><a>ABOUT US</a><a>SERVICES</a><a>BLOG</a><a>TESTIMONIALS</a><a>CONTACT US</a>
  </nav>
</header>

<section class="hero" role="img" aria-label="Dim photo of a modern rendered interior with pendant lights and a wood stove">
  <div class="hero-copy">
    <h1>RENDERING IN<br>CONSTRUCTION INDUSTRY</h1>
    <a class="btn">READ MORE</a>
  </div>
  <div class="dots"><span></span><span></span><span class="on"></span><span></span><span></span></div>
</section>

<section class="services">
  <h2 class="section-title">OUR SERVICES</h2>
  <div class="rule"></div>
  <div class="service-grid">
    <article class="service">
      <div class="ph" role="img" aria-label="Bright living room with smooth white plastered walls" style="background:linear-gradient(135deg,#e9ebec,#c9ced1)"></div>
      <h3>RENDERING</h3>
      <p>Lorem Ipsum is simply dummy text of the printing and typesetting industry</p>
      <a class="btn">READ MORE</a>
    </article>
    <article class="service">
      <div class="ph" role="img" aria-label="Room under construction with new plasterboard walls and ceiling" style="background:linear-gradient(135deg,#d9d9d6,#a9a7a1)"></div>
      <h3>WALL AND FLOOR SYSTEMS</h3>
      <p>Lorem Ipsum is simply dummy text of the printing and typesetting industry</p>
      <a class="btn">READ MORE</a>
    </article>
    <article class="service">
      <div class="ph" role="img" aria-label="Wall being boarded over insulation with ladders and tools" style="background:linear-gradient(135deg,#dedbd4,#c2a978)"></div>
      <h3>ACRYLIC RENDER HOUSES WALLS</h3>
      <p>Lorem Ipsum is simply dummy text of the printing and typesetting industry</p>
      <a class="btn">READ MORE</a>
    </article>
  </div>
</section>

<section class="about" role="img" aria-label="Builder in a hard hat fixing plasterboard over insulated wall">
  <div class="about-copy">
    <div class="eyebrow">ABOUT</div>
    <h2>KESTREL RENDERING</h2>
    <p>There are many variations of passages of Lorem Ipsum available, but the majority have suffered alteration in some form, by injected humour, or randomised words which don't look even slightly believable. If you are going to use a passage of Lorem Ipsum, you need to be sure there isn't anything embarrassing hidden.</p>
    <a class="btn">READ MORE</a>
  </div>
</section>

<section class="blog">
  <h2 class="section-title">LATEST BLOG</h2>
  <div class="rule"></div>
  <div class="blog-grid">
    <article class="post">
      <div class="ph" role="img" aria-label="Interior wall with insulation panels and ladders" style="background:linear-gradient(135deg,#dcd8d0,#b9a273)"></div>
      <h3>There are many variations of pass of Lorem Ipsum available but.</h3>
      <p>It is a long established fact that a reader will be Lorem Ipsum generato</p>
      <a class="btn">READ MORE</a>
    </article>
    <article class="post">
      <div class="ph" role="img" aria-label="Empty bright room with freshly finished walls" style="background:linear-gradient(135deg,#eef0f2,#bfc3c8)"></div>
      <h3>There are many variations of pass of Lorem Ipsum available but.</h3>
      <p>It is a long established fact that a reader will be Lorem Ipsum generato</p>
      <a class="btn">READ MORE</a>
    </article>
    <article class="post">
      <div class="ph" role="img" aria-label="Worker in a red hard hat plastering a wall" style="background:linear-gradient(135deg,#e6e4e1,#c99a86)"></div>
      <h3>There are many variations of pass of Lorem Ipsum available but.</h3>
      <p>It is a long established fact that a reader will be Lorem Ipsum generato</p>
      <a class="btn">READ MORE</a>
    </article>
  </div>
</section>

<section class="contact" role="img" aria-label="Greyscale photo of large rendered family houses">
  <div class="contact-card">
    <h2 class="section-title">QUICK CONTACT</h2>
    <div class="rule"></div>
    <form class="form">
      <div class="row"><div class="field">Name</div><div class="field">E mail Id</div></div>
      <div class="row"><div class="field">Phone</div><div class="field">Subject</div></div>
      <div class="row"><div class="field area">Mesage</div></div>
      <a class="btn">SUBMIT</a>
    </form>
  </div>
</section>

<footer class="site-footer">
  <div class="footer-brand">
    <div class="brand-mark"></div>
    <div class="brand-name">KESTREL<br>RENDERING</div>
  </div>
  <div class="license">LIC 40218-3300 555-014-7720</div>

  <div class="col col-contact">
    <h4>CONTACT US</h4>
    <div class="c-item">
      <svg width="10" height="12" viewBox="0 0 24 30"><path fill="#fff" d="M12 0a10 10 0 0 0-10 10c0 8 10 20 10 20s10-12 10-20A10 10 0 0 0 12 0zm0 14a4 4 0 1 1 0-8 4 4 0 0 1 0 8z"/></svg>
      <span>58 Foundry Lane<br>Millbrook, IL 60999</span>
    </div>
    <div class="c-item">
      <svg width="11" height="11" viewBox="0 0 24 24"><path fill="#fff" d="M6.6 10.8a15.1 15.1 0 0 0 6.6 6.6l2.2-2.2c.3-.3.7-.4 1-.2 1.1.4 2.3.6 3.6.6.6 0 1 .4 1 1V20c0 .6-.4 1-1 1C10.6 21 3 13.4 3 4c0-.6.4-1 1-1h3.5c.6 0 1 .4 1 1 0 1.3.2 2.5.6 3.6.1.3 0 .7-.2 1z"/></svg>
      <span>555.014.2288</span>
    </div>
    <div class="c-item">
      <svg width="12" height="10" viewBox="0 0 24 18"><rect width="24" height="18" rx="2" fill="#fff"/><path d="M1 2l11 8 11-8" fill="none" stroke="#1c2430" stroke-width="2"/></svg>
      <span>info@kestrelrendering.com</span>
    </div>
  </div>

  <div class="col col-menu">
    <h4>MENU</h4>
    <ul><li>Home</li><li>About Us</li><li>Services</li><li>Blog</li><li>Testimonials</li><li>Contact us</li></ul>
  </div>

  <div class="col col-news">
    <h4>NEWSLETTER</h4>
    <div class="field">E mail id</div>
    <a class="btn">SIGNUP</a>
  </div>

  <div class="footer-rule"></div>
  <div class="follow">FOLLOW US
    <span class="dot" style="background:#3b5998"></span>
    <span class="dot" style="background:#1da1f2"></span>
    <span class="dot" style="background:#1f3f8f"></span>
  </div>
  <div class="copyright">Copyrights @ 2017 All Rights Reserved</div>
</footer>

</body>
</html>
```